BlueCedar Massage Studio

We need a double sided full colour post card sized flyer for a pro women (women only) sports and remedial massage studio based in Singapore. It's a small and boutique business promoting itself to a very local audience i.e. Within walking distance of the massage studio.

The attached logo and photo are to be integrated into the overall theme which should offer a simple, attractive, elegant and professional/sporty feel.

Funky, eclectic and/or retro options all welcome.

The company website is www.bluecedar-example.com.sg for reference purposes (in case Orbit Domainhouse hasn't uploaded it yet, FB page is live; Facebook.com/bluecedarmassage). The main means of booking will be call or WhatsApp to 9000 1234 or visit the website.

Ideally there would be a white border around the postcard rather than a full bleed option.

This will be used in a mail drop environment and therefore needs to have a call to action clearly (but elegantly) displayed so as to grab attention. It needs to send the message, 'on your doorstep, female sports massage' - obviously, you have poetic license with the wording.

It is our plan that we would use a personalised stamp for special offers on the reverse side but only on one half/side - we need you to include the location map as per the web site on the other half/side.

The strap line used by Blue Cedar is 'Feel better, move better, perform better'. This should be incorporated low down, and subtly on the front side.

Target Market(s)

Women. Sports orientated. Adults, professionals and ex-pats

Requirements
Must have
• Call to action. Needs to be attention grabbing in a fun, elegant way

```html
<!DOCTYPE html>
<html lang="en">
<head>
<meta charset="utf-8">
<title>Blue Cedar – Postcard Flyer</title>
<link href="https://fonts.googleapis.com/css2?family=Open+Sans:wght@400;600;700&family=Roboto+Condensed:wght@700&display=swap" rel="stylesheet">
<style>
  :root{
    --stage:#000000;
    --label:#e0201b;
    --paper:#ffffff;
    --brand-pink:#e8127f;
    --brand-green:#7dc242;
    --ink:#3b3b3b;
    --ink-dark:#1c1c1c;
    --sky-top:#a9d3ea;
    --sky-mid:#cfe6f2;
    --sea:#3fb6c8;
    --sea-deep:#1f8fa8;
    --map-light:#e6e6e6;
    --map-dark:#d6d6d6;
    --box-line:#b9b9b9;
  }
  *{box-sizing:border-box;margin:0;padding:0}
  html,body{width:764px;height:1200px;overflow:hidden;background:var(--stage)}
  body{position:relative;font-family:"Open Sans",Arial,sans-serif}

  .side-label{position:absolute;left:0;width:764px;text-align:center;
    color:var(--label);font-size:17px;letter-spacing:.5px}
  .side-label--front{top:20px}
  .side-label--back{top:585px}

  .postcard{position:absolute;left:57px;width:649px;height:504px;background:var(--paper)}
  .postcard--front{top:53px}
  .postcard--back{top:615px;height:503px}

  /* front */
  .hero{position:absolute;left:14px;top:16px;width:619px;height:425px;overflow:hidden}
  .hero__photo{position:absolute;inset:0;
    background:
      radial-gradient(ellipse 150px 230px at 150px 230px,rgba(214,150,125,.55) 0%,rgba(214,150,125,0) 100%),
      linear-gradient(180deg,var(--sky-top) 0%,var(--sky-mid) 52%,var(--sea) 66%,var(--sea-deep) 100%)}
  .hero__copy{position:absolute;left:433px;top:0;width:186px;height:425px;color:var(--ink)}
  .brand{position:absolute;font-weight:700;color:var(--brand-pink);letter-spacing:-1px;line-height:1}
  .brand__sub{position:absolute;font-size:11px;color:var(--ink);white-space:nowrap}
  .hero .brand{left:0;top:24px;font-size:30px}
  .hero .brand__sub{left:1px;top:58px;font-size:10.5px}
  .rule{position:absolute;left:0;width:186px;height:2px;background:var(--paper)}
  .rule--top{top:75px}
  .rule--mid{top:306px}
  .headline{position:absolute;left:0;top:82px;line-height:1.05;text-transform:uppercase}
  .headline__line{display:block;font-size:31px;font-weight:400;color:var(--ink)}
  .headline__accent{display:block;font-size:20px;font-weight:600;color:var(--brand-pink);margin-top:4px}
  .headline__key{display:block;font-size:31px;font-weight:700;color:var(--brand-green)}
  .cta{position:absolute;left:0;top:312px}
  .cta__label{font-size:21px;font-weight:700;color:var(--brand-pink);text-transform:uppercase}
  .cta__phone{font-family:"Roboto Condensed","Arial Narrow",sans-serif;font-size:36px;font-weight:700;color:var(--ink-dark);line-height:1.1}

  .strapline{position:absolute;left:14px;width:619px;height:43px;display:flex;
    justify-content:center;align-items:center;gap:22px;color:var(--paper);
    font-size:16px;text-transform:uppercase;letter-spacing:.3px}
  .strapline--pink{top:444px;background:var(--brand-pink)}
  .strapline--green{top:445px;background:var(--brand-green)}
  .strapline__item{display:flex;align-items:center;gap:8px}
  .strapline__item svg{width:13px;height:13px}

  /* back */
  .address-box{position:absolute;left:16px;top:33px;width:263px;height:392px;
    border:1.5px solid var(--box-line);border-radius:8px}
  .postcard--back .brand{left:319px;top:47px;font-size:34px}
  .postcard--back .brand__sub{left:320px;top:85px;font-size:12px}
  .stamp-box{position:absolute;left:520px;top:36px;width:85px;height:103px;
    border:1.5px solid var(--box-line)}
  .location-map{position:absolute;left:302px;top:167px;width:316px;height:252px;
    background:linear-gradient(135deg,var(--map-light) 0%,var(--map-dark) 100%);
    border-radius:4px}
</style>
</head>
<body>
  <div class="side-label side-label--front">FRONT</div>

  <section class="postcard postcard--front">
    <div class="hero">
      <div class="hero__photo" role="img" aria-label="Photo of an athletic woman seen from behind in sports top and pink shorts, hands on her lower back, beside a blue sea"></div>
      <div class="hero__copy">
        <div class="brand">bluecedar</div>
        <div class="brand__sub">Remedial and sports massage</div>
        <div class="rule rule--top"></div>
        <h1 class="headline">
          <span class="headline__line">On your</span>
          <span class="headline__line">doorstep</span>
          <span class="headline__accent">Female sports</span>
          <span class="headline__key">Massage</span>
        </h1>
        <div class="rule rule--mid"></div>
        <div class="cta">
          <div class="cta__label">Book today</div>
          <div class="cta__phone">9000 1234</div>
        </div>
      </div>
    </div>
    <div class="strapline strapline--pink">
      <span class="strapline__item"><svg viewBox="0 0 14 14"><circle cx="7" cy="7" r="6" fill="#fff"/><path d="M5.5 4l3 3-3 3" stroke="#e8127f" stroke-width="1.8" fill="none"/></svg>Feel better</span>
      <span class="strapline__item"><svg viewBox="0 0 14 14"><circle cx="7" cy="7" r="6" fill="#fff"/><path d="M5.5 4l3 3-3 3" stroke="#e8127f" stroke-width="1.8" fill="none"/></svg>Move better</span>
      <span class="strapline__item"><svg viewBox="0 0 14 14"><circle cx="7" cy="7" r="6" fill="#fff"/><path d="M5.5 4l3 3-3 3" stroke="#e8127f" stroke-width="1.8" fill="none"/></svg>Perform better</span>
    </div>
  </section>

  <div class="side-label side-label--back">BACK</div>

  <section class="postcard postcard--back">
    <div class="address-box"></div>
    <div class="brand">bluecedar</div>
    <div class="brand__sub">Remedial and sports massage</div>
    <div class="stamp-box"></div>
    <div class="location-map" role="img" aria-label="Street map of the neighbourhood with a pin marking the studio location next to the park"></div>
    <div class="strapline strapline--green">
      <span class="strapline__item"><svg viewBox="0 0 14 14"><circle cx="7" cy="7" r="6" fill="#fff"/><path d="M5.5 4l3 3-3 3" stroke="#7dc242" stroke-width="1.8" fill="none"/></svg>Feel better</span>
      <span class="strapline__item"><svg viewBox="0 0 14 14"><circle cx="7" cy="7" r="6" fill="#fff"/><path d="M5.5 4l3 3-3 3" stroke="#7dc242" stroke-width="1.8" fill="none"/></svg>Move better</span>
      <span class="strapline__item"><svg viewBox="0 0 14 14"><circle cx="7" cy="7" r="6" fill="#fff"/><path d="M5.5 4l3 3-3 3" stroke="#7dc242" stroke-width="1.8" fill="none"/></svg>Perform better</span>
    </div>
  </section>
</body>
</html>
```